New Company Business Card Design

I have a new company logo and I want a new business card design. I dont know if the logo file i attached is in the correct format or quality. We are a New York City Specialty construction Firm specializing in high risk out of the box projects. I want a simple and classy business card that people will his card is as crisp as the work his company does.

Target Market(s)

Clients in the heavy construction industry in New York City

Industry/Entity Type

Construction Company

Contact Information for Business Card

Simple Classy - DIFFERENT

Font styles to use
Other font styles liked:
• Mach the logo font in some way

Colors

Designer to choose colors to be used in the design.

Requirements
Must have
• Uniqueness
Nice to have
• Nothing particular - Just different and classy - Timeless
Should not have
• Goofy Shit or Gimmicky shit

```html
<!DOCTYPE html>
<html lang="en">
<head>
<meta charset="utf-8">
<title>Korvel Builders – Business Card</title>
<link rel="stylesheet" href="https://fonts.googleapis.com/css2?family=Roboto:wght@400;500;700&family=Montserrat:wght@500&display=swap">
<style>
  :root {
    --backdrop: #323232;
    --card-white: #f3f3f3;
    --card-black: #151515;
    --brand-blue: #1f6fb8;
    --text-grey: #4a4a4a;
    --rule-grey: #9a9a9a;
    --white: #ffffff;
  }
  * { margin: 0; padding: 0; box-sizing: border-box; }
  html, body {
    width: 1200px; height: 986px; overflow: hidden;
    background: var(--backdrop);
    font-family: "Roboto", Arial, sans-serif;
  }
  .canvas { position: relative; width: 1200px; height: 986px; }
  .card {
    position: absolute; left: 342px; width: 517px; height: 296px;
  }
  .card--front { top: 160px; background: var(--card-white); }
  .card--back {
    top: 530px;
    background: radial-gradient(ellipse at 50% 40%, #222 0%, var(--card-black) 70%);
  }

  .wordmark {
    font-family: "Roboto", Arial, sans-serif;
    font-weight: 700;
    color: var(--brand-blue);
    text-transform: uppercase;
    line-height: 1;
  }
  .card--front .wordmark {
    position: absolute; right: 36px; top: 56px;
    font-size: 30px; text-align: right; letter-spacing: 1px;
  }
  .card--front .wordmark span { display: block; font-size: 13px; letter-spacing: 4px; margin-top: 8px; }

  .holder { position: absolute; left: 30px; top: 133px; }
  .holder__name { font-size: 20px; font-weight: 500; color: var(--brand-blue); letter-spacing: -0.2px; }
  .holder__title { font-size: 14px; color: var(--text-grey); margin-top: 2px; }

  .divider { position: absolute; left: 30px; top: 186px; width: 451px; height: 3px; }
  .divider__accent { position: absolute; left: 0; top: 0; width: 62px; height: 3px; background: var(--brand-blue); }
  .divider__line { position: absolute; left: 66px; top: 1px; right: 0; height: 1px; background: var(--rule-grey); }

  .contacts { position: absolute; left: 30px; top: 205px; list-style: none; }
  .contacts li {
    display: flex; align-items: center; gap: 6px;
    font-size: 12px; color: var(--text-grey); height: 17.6px;
  }
  .contacts svg { width: 11px; height: 11px; fill: var(--brand-blue); flex: none; }

  .address {
    position: absolute; right: 36px; top: 236px;
    font-size: 12px; color: var(--text-grey); text-align: right; line-height: 17px;
    font-style: normal;
  }

  .card--back .wordmark {
    position: absolute; left: 0; right: 0; top: 118px;
    text-align: center; font-size: 46px; letter-spacing: 2px;
  }
  .card--back .wordmark span { display: block; font-size: 15px; letter-spacing: 7px; margin-top: 10px; }
  .back__url {
    position: absolute; left: 0; right: 0; top: 254px;
    text-align: center; font-family: "Montserrat", Arial, sans-serif;
    font-size: 12px; font-weight: 500; letter-spacing: 2.5px; color: var(--white);
  }
</style>
</head>
<body>
<main class="canvas">
  <section class="card card--front" aria-label="Business card front">
    <div class="wordmark">Korvel<span>Builders, Inc.</span></div>

    <div class="holder">
      <h1 class="holder__name">Marcus T. Ellery</h1>
      <p class="holder__title">President</p>
    </div>

    <div class="divider"><div class="divider__accent"></div><div class="divider__line"></div></div>

    <ul class="contacts">
      <li><svg viewBox="0 0 24 24"><path d="M6.6 10.8a15.1 15.1 0 0 0 6.6 6.6l2.2-2.2a1 1 0 0 1 1-.25 11.4 11.4 0 0 0 3.6.57 1 1 0 0 1 1 1V20a1 1 0 0 1-1 1A17 17 0 0 1 3 4a1 1 0 0 1 1-1h3.5a1 1 0 0 1 1 1c0 1.25.2 2.45.57 3.57a1 1 0 0 1-.25 1z"/></svg>555-014-2270</li>
      <li><svg viewBox="0 0 24 24"><path d="M7 1h10a2 2 0 0 1 2 2v18a2 2 0 0 1-2 2H7a2 2 0 0 1-2-2V3a2 2 0 0 1 2-2zm0 3v14h10V4zm5 15.5a1.2 1.2 0 1 0 0 2.4 1.2 1.2 0 0 0 0-2.4z"/></svg>555-017-3381</li>
      <li><svg viewBox="0 0 24 24"><path d="M2 5h20v14H2zm2 2v.5l8 5 8-5V7l-8 5z"/></svg>MARCUS@KORVEL.COM</li>
      <li><svg viewBox="0 0 24 24"><path d="M12 2a10 10 0 1 0 0 20 10 10 0 0 0 0-20zm6.9 6h-2.9a15 15 0 0 0-1.3-3.6A8 8 0 0 1 18.9 8zM12 4c.8 1.2 1.5 2.5 1.9 4h-3.8c.4-1.5 1.1-2.8 1.9-4zM4.3 14a8 8 0 0 1 0-4h3.3a16 16 0 0 0 0 4zm.8 2h2.9c.3 1.3.8 2.5 1.3 3.6A8 8 0 0 1 5.1 16zM8 8H5.1a8 8 0 0 1 4.2-3.6C8.8 5.5 8.3 6.7 8 8zm4 12c-.8-1.2-1.5-2.5-1.9-4h3.8c-.4 1.5-1.1 2.8-1.9 4zm2.3-6H9.7a14 14 0 0 1 0-4h4.6a14 14 0 0 1 0 4zm.4 5.6c.5-1.1 1-2.3 1.3-3.6h2.9a8 8 0 0 1-4.2 3.6zm1.7-5.6a16 16 0 0 0 0-4h3.3a8 8 0 0 1 0 4z"/></svg>KORVEL.COM</li>
    </ul>

    <address class="address">48 Harbor Yard Road<br>Linden, New Jersey 07036</address>
  </section>

  <section class="card card--back" aria-label="Business card back">
    <div class="wordmark">Korvel<span>Builders, Inc.</span></div>
    <p class="back__url">KORVEL.COM</p>
  </section>
</main>
</body>
</html>
```